Postcard Design Project

Education- charter school- elementary k-6th grades- performing arts integrated in to the core curriculum

Industry/Entity Type

School

```html
<!DOCTYPE html>
<html lang="en">
<head>
<meta charset="utf-8">
<title>Bright Steps Arts Academy – Now Enrolling</title>
<link rel="stylesheet" href="https://fonts.googleapis.com/css2?family=Ubuntu:wght@700&family=PT+Sans:wght@400&display=swap">
<style>
  :root {
    --paper: #ffffff;
    --band-purple-start: #a04e9f;
    --band-purple-end: #8f4fa1;
    --deep-violet: #5e4fa3;
    --ink-navy: #2d265c;
    --sun-yellow: #e9da14;
    --mist: #dbeef6;
    --brand-ink: #4a3a8c;
    --headline: #ffffff;
  }
  * { margin: 0; padding: 0; box-sizing: border-box; }
  html, body { width: 861px; height: 1200px; overflow: hidden; background: var(--paper); }
  .postcard {
    position: relative;
    width: 861px;
    height: 1200px;
    background: var(--paper);
    overflow: hidden;
    font-family: "PT Sans", sans-serif;
  }
  .backdrop { position: absolute; inset: 0; width: 100%; height: 100%; }
  .brand {
    position: absolute;
    left: 0; width: 588px;
    top: 160px;
    display: flex; align-items: center; justify-content: center; gap: 10px;
  }
  .brand-dot {
    width: 18px; height: 18px; border-radius: 50%;
    background: var(--deep-violet);
  }
  .brand-name {
    font-family: "PT Sans", sans-serif;
    font-size: 21px;
    color: var(--brand-ink);
  }
  .headline {
    position: absolute;
    left: 397px; top: 248px;
    color: var(--headline);
    font-family: "Ubuntu", sans-serif;
    font-weight: 700;
    font-size: 54px;
    line-height: 80px;
  }
  .activity-photo {
    position: absolute;
    left: 90px; top: 500px;
    width: 771px; height: 430px;
    background: radial-gradient(ellipse at 50% 55%, rgba(240,150,70,0.35), rgba(120,150,210,0.25) 45%, rgba(255,255,255,0) 72%);
  }
  .school-block {
    position: absolute;
    left: 299px; top: 952px;
    color: var(--brand-ink);
  }
  .school-name {
    font-size: 35px;
    line-height: 42px;
    font-weight: 400;
  }
  .school-contact {
    margin-top: 14px;
    font-size: 22px;
    line-height: 27px;
    font-style: normal;
  }
</style>
</head>
<body>
<main class="postcard">
  <svg class="backdrop" viewBox="0 0 873 1280" preserveAspectRatio="none" aria-hidden="true">
    <defs>
      <linearGradient id="bandFill" x1="0" y1="0" x2="1" y2="0">
        <stop offset="0" stop-color="var(--band-purple-start)"/>
        <stop offset="1" stop-color="var(--band-purple-end)"/>
      </linearGradient>
      <linearGradient id="mistFill" x1="0" y1="0" x2="1" y2="0">
        <stop offset="0" stop-color="var(--mist)" stop-opacity="0.9"/>
        <stop offset="1" stop-color="var(--mist)" stop-opacity="0.2"/>
      </linearGradient>
    </defs>
    <polygon class="mist-strip" points="0,250 873,170 873,200 0,310" fill="url(#mistFill)"/>
    <polygon class="enrol-band" points="0,307 873,172 873,665 0,383" fill="url(#bandFill)"/>
    <polygon class="mist-strip" points="250,495 873,650 873,700" fill="url(#mistFill)"/>
    <polygon class="navy-sliver" points="300,520 873,700 873,790" fill="var(--ink-navy)"/>
    <polygon class="violet-wedge" points="873,730 873,800 560,700" fill="var(--deep-violet)" opacity="0.85"/>
    <polygon class="violet-edge" points="0,680 95,935 0,1250" fill="var(--deep-violet)"/>
    <polygon class="violet-stripe" points="120,900 320,1280 220,1280" fill="var(--deep-violet)"/>
    <polygon class="sun-corner" points="873,920 873,1280 655,1280" fill="var(--sun-yellow)"/>
    <polygon class="mist-strip" points="600,1280 873,900 873,960 660,1280" fill="url(#mistFill)"/>
  </svg>

  <header class="brand">
    <span class="brand-dot"></span>
    <span class="brand-name">Bright Steps Arts Academy</span>
  </header>

  <h1 class="headline">Now Enrolling<br>2016-17 for<br>Grades k-6th</h1>

  <div class="activity-photo" role="img" aria-label="Photo of a row of joyful children jumping in the air in colourful clothes, with a flowing music staff and notes behind them"></div>

  <section class="school-block">
    <h2 class="school-name">Bright Steps Arts Academy<br>Community School</h2>
    <address class="school-contact">
      250 Maple Grove Lane<br>
      Riverton, Ohio 43000<br>
      Phone: (555) 014-2290
    </address>
  </section>
</main>
</body>
</html>
```